private relaxation massage therapist business card

I want a card that does not give a physical address as I am able to massage at home as well as be mobile. I want on the back somewhere to put appointment details and also my bank acct details for payment being to acct 38 6042 0071846 00
I have a Certificate in Relaxation Massage from KTRB 2014
I would like to use blue colours and maybe have some fluffy clouds somewhere on the business card.

Industry/Entity Type

Massage

Contact Information for Business Card

Megan Pollard
Relaxation Massage Therapist

telephone 0218 647 092 or 09 8416375
email meganpollard72@quillmail.com

Requirements
Must have
• bold lettering, lots of white space, On the reverse of the card some lines in a box for me to write appointment times also on reverse my bank acct details for payment on line.

```html
<!DOCTYPE html>
<html lang="en">
<head>
<meta charset="utf-8">
<title>Appointment Card – Reverse</title>
<link href="https://fonts.googleapis.com/css2?family=Lustria&display=swap" rel="stylesheet">
<style>
  :root {
    --backdrop: #647f95;
    --card-white: #ffffff;
    --brand-blue: #0069b4;
    --rule-blue: #4f7ac4;
    --edge-red: #c0504d;
  }
  html, body {
    margin: 0;
    padding: 0;
    width: 1200px;
    height: 741px;
    overflow: hidden;
    background: var(--backdrop);
  }
  .canvas {
    position: relative;
    width: 1200px;
    height: 741px;
    font-family: "Lustria", "Georgia", serif;
  }
  .card {
    position: absolute;
    left: 17px;
    top: 17px;
    width: 1166px;
    height: 705px;
    background: var(--card-white);
    outline: 1px solid var(--edge-red);
  }
  .notes-frame {
    position: absolute;
    left: 23px;
    top: 20px;
    width: 643px;
    height: 666px;
    box-sizing: border-box;
    border: 15px solid var(--brand-blue);
    border-top-width: 21px;
    border-bottom-width: 18px;
    border-right: none;
  }
  .payment-panel {
    position: absolute;
    left: 666px;
    top: 0;
    width: 500px;
    height: 705px;
    background: var(--brand-blue);
  }
  .payment-frame {
    position: absolute;
    left: 0;
    top: 20px;
    width: 474px;
    height: 666px;
    box-sizing: border-box;
    border: 18px solid var(--card-white);
    border-left: none;
    border-top-width: 20px;
    border-bottom-width: 19px;
  }
  .notes-heading {
    position: absolute;
    left: 66px;
    top: 82px;
    margin: 0;
    font-weight: 400;
    font-size: 46px;
    line-height: 1;
    color: var(--brand-blue);
    white-space: nowrap;
  }
  .writing-lines {
    position: absolute;
    left: 0;
    top: 0;
  }
  .payment-details {
    position: absolute;
    left: 679px;
    top: 295px;
    margin: 0;
    color: var(--card-white);
    font-size: 43px;
    letter-spacing: 1px;
    line-height: 58px;
    white-space: nowrap;
  }
  .payment-details .account-number {
    display: block;
    margin-left: -3px;
    font-size: 45px;
    letter-spacing: 2px;
  }
</style>
</head>
<body>
<div class="canvas">
  <div class="card">
    <div class="notes-frame"></div>
    <div class="payment-panel">
      <div class="payment-frame"></div>
    </div>

    <h2 class="notes-heading">Appointment details:</h2>

    <svg class="writing-lines" width="1166" height="705" viewBox="0 0 1166 705" aria-hidden="true">
      <g stroke="var(--rule-blue)" stroke-width="3" stroke-linecap="round">
        <line x1="70" y1="195" x2="635" y2="195"/>
        <line x1="70" y1="254" x2="635" y2="254"/>
        <line x1="70" y1="312" x2="635" y2="312"/>
        <line x1="70" y1="371" x2="635" y2="371"/>
        <line x1="70" y1="430" x2="635" y2="430"/>
        <line x1="70" y1="489" x2="635" y2="489"/>
        <line x1="70" y1="548" x2="635" y2="548"/>
        <line x1="70" y1="606" x2="635" y2="606"/>
      </g>
    </svg>

    <p class="payment-details">
      Payment @ A/C:
      <span class="account-number">38 6042 0071846 00</span>
    </p>
  </div>
</div>
</body>
</html>
```